Landing Page für Freelancer im Bereich der Informationstechnik
Zielgruppe
Ich bin Experte für Informationstechnik, Unified Communications, Beratung, Management sowie Projekte aller Art.
Mit meiner WOLKENTOR GmbH bin ich als (einzelner) Freelancer für mittelständische Unternehmen und Konzerne in verschiedensten Projekten tätig.
Mein Motto lautet 'Mit Präzision und langjähriger Erfahrung immer alles im Griff!'
Aufgabenstellung
Die aktuell existierende Internet-Präsenz unter wolkentor-beispiel.de beinhaltet aktuell nur eine minimalistische statische Seite sowie das Impressum, ohne jegliche dynamische Inhalte.
DABEI SOLL ES BLEIBEN. Auch die Inhalte sollen unverändert übernommen werden.
Lediglich soll jetzt eine Anlehnung an das zwischenzeitlich vorhandene Logo vorgenommen werden, welches ich mitliefere.
Es geht mir insgesamt nur darum, ein professionelleres Auftreten zu haben, WENN sich denn mal jemand auf die Seite verirrt.
Das Aussehen soll daher modern und dynamisch sein.
ZUSAMMENFASSUNG: Inhalte bleiben 1:1, grafische Anpassung an Logo gewünscht.
Technisch: Statisch, kein Content-Management. Lohnt sich hier nicht.
SEHR WICHTIG: Ich möchte gerne, dass die Lieferung bereits als HTML (und NICHT NUR ALS GRAFIK) erfolgt, ggf. stelle ich auch kurz den FTP-Zugang.
Insgesamt möchte ich gar keine große Sache draus machen.
Viele Anpassungsrunden wird es voraussichtlich nicht geben.
Zeitlich ist dies hier ein sehr kleines Projekt - Erweiterungen kommen später.

```html
<!DOCTYPE html>
<html lang="de">
<head>
<meta charset="utf-8">
<title>WOLKENTOR GmbH – Malte Johannes Brandt</title>
<link rel="stylesheet" href="https://fonts.googleapis.com/css2?family=Outfit:wght@500;600&display=swap">
<style>
  :root {
    --text: #454545;
    --accent: #4ea7c0;
    --bg: #ffffff;
    --photo-light: #fbfbfb;
    --photo-mid: #f1efef;
  }
  * { margin: 0; padding: 0; box-sizing: border-box; }
  html, body { width: 1113px; height: 1200px; overflow: hidden; background: var(--bg); }
  body { position: relative; font-family: "Outfit", sans-serif; color: var(--text); font-weight: 600; }

  .brand { position: absolute; left: 108px; top: 66px; display: flex; align-items: center; gap: 8px; }
  .brand-dot { width: 14px; height: 14px; border-radius: 50%; background: var(--accent); }
  .brand-name { font-size: 15px; font-weight: 600; color: var(--accent); letter-spacing: 0.06em; }

  .site-nav { position: absolute; top: 73px; right: 103px; display: flex; gap: 35px; }
  .site-nav a { font-size: 12.5px; color: var(--text); text-decoration: none; }

  .degree { position: absolute; left: 108px; font-size: 22px; }
  .degree-fh { top: 158px; }
  .degree-msc { top: 276px; }
  .person-name { position: absolute; left: 107px; top: 204px; font-size: 42px; color: var(--accent); font-weight: 600; letter-spacing: -0.005em; }

  .contact-mail { position: absolute; left: 108px; top: 388px; font-size: 11.5px; color: var(--text); text-decoration: none; border-bottom: 1px solid var(--accent); padding-bottom: 1px; }

  .intro { position: absolute; left: 455px; top: 383px; width: 560px; }
  .intro-heading { font-size: 30px; line-height: 42px; font-weight: 600; }
  .intro-text { margin-top: 28px; font-size: 11.8px; line-height: 19.5px; font-weight: 500; width: 555px; }
  .motto { margin-top: 54px; font-size: 19px; line-height: 29px; text-transform: uppercase; font-weight: 600; letter-spacing: -0.01em; }
  .motto .quote-mark { color: var(--accent); }

  .hero-photo { position: absolute; left: 108px; top: 773px; width: 902px; height: 349px;
    background: radial-gradient(ellipse at 75% 60%, var(--photo-mid), var(--photo-light) 70%); }
</style>
</head>
<body>
  <div class="brand">
    <span class="brand-dot"></span>
    <span class="brand-name">WOLKENTOR GmbH</span>
  </div>

  <nav class="site-nav">
    <a href="#">Impressum</a>
    <a href="#">Datenschutz</a>
  </nav>

  <p class="degree degree-fh">Diplom-Informatiker (FH)</p>
  <h1 class="person-name">Malte Johannes Brandt</h1>
  <p class="degree degree-msc">Master of Science in Electronic Business</p>

  <a class="contact-mail" href="#">m punkt brandt at wolkentor-beispiel punkt de</a>

  <section class="intro">
    <h2 class="intro-heading">Experte für Informationstechnik | Unified Communications | Beratung | Management | Projekte aller Art</h2>
    <p class="intro-text">Gerne schicke ich Ihnen unverbindlich mein Expertenprofil samt CV sowie meine aktuellen Verfügbarkeiten zu. Kontaktieren Sie mich hierzu einfach per E-Mail unter m punkt brandt at wolkentor-beispiel punkt de. Ich freue mich auf Sie!</p>
    <p class="motto"><span class="quote-mark">"</span>Mit Präzision und langjähriger<br>Erfahrung immer alles im Griff!<span class="quote-mark">"</span></p>
  </section>

  <div class="hero-photo" role="img" aria-label="Foto: Kaffeetasse mit schwarzem Kaffee von oben auf hellem Tisch"></div>
</body>
</html>
```